2m x 3m Trade Show Booth Design

We have a Hospitality Trade Show with a 2m x 3m spot. Two side walls of 2m and one back wall of 3m. Need artwork to be printed on vinyl and attached. Please see attached docs for existing media, logos, etc

```html
<!DOCTYPE html>
<html lang="en">
<head>
<meta charset="UTF-8">
<title>TillMedic – Trade Show Wall</title>
<link href="https://fonts.googleapis.com/css2?family=Poppins:wght@600;700;800&family=Inter:wght@500&display=swap" rel="stylesheet">
<style>
  :root {
    --navy: #1b3a6b;
    --teal: #2bb0b4;
    --teal-deep: #1f8f96;
    --teal-light: #7fd3d3;
    --paper: #ffffff;
    --backdrop: #e9e9e9;
  }
  html, body {
    margin: 0;
    padding: 0;
    width: 1200px;
    height: 1200px;
    overflow: hidden;
    background: var(--backdrop);
  }
  .wall {
    position: absolute;
    left: 0;
    top: 201px;
    width: 1200px;
    height: 798px;
    background: var(--paper);
    font-family: "Poppins", sans-serif;
  }
  .brand-name {
    position: absolute;
    left: 54px;
    top: 66px;
    margin: 0;
    font-size: 104px;
    font-weight: 600;
    line-height: 1;
    letter-spacing: -2px;
    color: var(--navy);
    white-space: nowrap;
  }
  .brand-rule {
    position: absolute;
    left: 54px;
    top: 204px;
    width: 555px;
    height: 2px;
    background: var(--teal);
  }
  .brand-tagline {
    position: absolute;
    left: 54px;
    top: 216px;
    margin: 0;
    font-family: "Inter", sans-serif;
    font-weight: 500;
    font-size: 25px;
    line-height: 1.2;
    color: var(--navy);
    white-space: nowrap;
  }
  .headline {
    position: absolute;
    left: 56px;
    top: 318px;
    margin: 0;
    font-weight: 800;
    line-height: 1;
    text-transform: uppercase;
    white-space: nowrap;
  }
  .headline > .line { display: block; }
  .headline .line-your {
    font-size: 153px;
    color: var(--teal);
    letter-spacing: 1px;
  }
  .headline .line-hospitality {
    margin-top: -9px;
    font-size: 71px;
    font-weight: 700;
    color: var(--navy);
    letter-spacing: 1px;
  }
  .headline .line-tech {
    margin-top: 0;
    font-size: 60px;
    font-weight: 700;
    color: var(--navy);
    letter-spacing: 1px;
  }
  .headline .accent { display: inline; color: var(--teal); }
  .values {
    position: absolute;
    left: 56px;
    top: 651px;
    margin: 0;
    font-weight: 700;
    font-size: 46px;
    line-height: 1;
    color: var(--navy);
    letter-spacing: 0.5px;
    white-space: nowrap;
  }
  .mascot {
    position: absolute;
    left: 618px;
    top: 51px;
    width: 530px;
    height: 697px;
  }
</style>
</head>
<body>
  <main class="wall">
    <h1 class="brand-name">TillMedic</h1>
    <div class="brand-rule"></div>
    <p class="brand-tagline">Hospitality IT, POS &amp; Network Specialists</p>

    <h2 class="headline">
      <span class="line line-your">Your</span>
      <span class="line line-hospitality">Hospitality</span>
      <span class="line line-tech">Tech <span class="accent">Doctor</span>.</span>
    </h2>

    <p class="values">FAST. LOCAL. RELIABLE.</p>

    <svg class="mascot" viewBox="0 0 530 697" role="img" aria-label="Illustrated technician mascot in a teal cap and hoodie, arms crossed, holding a card payment terminal and a barcode scanner">
      <defs>
        <linearGradient id="mascotTone" x1="0" y1="0" x2="0" y2="1">
          <stop offset="0" stop-color="#7fd3d3"/>
          <stop offset="1" stop-color="#1f8f96"/>
        </linearGradient>
      </defs>
      <rect x="0" y="0" width="530" height="697" rx="24" fill="url(#mascotTone)"/>
    </svg>
  </main>
</body>
</html>
```